VOLQ Marketing Sell Sheets Design

I need a flyer that I can use to market and advertise my business utilizing the logo that you already created. I will attach in detail a copy of the design specifics for the layout of the flyer as well as the content of each flyer. The color scheme will be the same as the logo you designed. Blues, greys, blacks, White

Target Market(s)

Insurance

Industry/Entity Type

Insurance Blue

Font styles to use
Sans Serif

Colors
3176b5
cfdeed
eaf1f7

Requirements
Must have
• I need 6 individual sheets on 8.5 X 11. The layout will be as per the layout I have marked up and described in the brief. The only change on each flyer is the content which I have submitted 6 descriptions along with content. The logo and color scheme will be as described In the brief.
Nice to have
• No preference
Should not have
• No preference

```html
<!DOCTYPE html>
<html lang="en">
<head>
<meta charset="utf-8">
<title>VOLQ Marketing – Sell Sheet</title>
<link rel="stylesheet" href="https://fonts.googleapis.com/css2?family=Roboto+Condensed:wght@300;400;700&display=swap">
<style>
  :root {
    --brand-blue: #3176b5;
    --blue-pale: #cfdeed;
    --blue-mist: #eaf1f7;
    --ink: #111111;
    --body-grey: #6f6f6f;
    --paper: #ffffff;
    --footer-black: #000000;
  }
  * { margin: 0; padding: 0; box-sizing: border-box; }
  html, body {
    width: 869px;
    height: 1200px;
    overflow: hidden;
    background: var(--paper);
  }
  .sheet {
    position: relative;
    width: 869px;
    height: 1200px;
    background: var(--paper);
    font-family: "Roboto Condensed", "Arial Narrow", sans-serif;
  }
  .top-band {
    position: absolute;
    left: 0; top: 0;
    width: 100%;
    height: 33px;
    background: var(--brand-blue);
  }
  .bottom-band {
    position: absolute;
    left: 0; bottom: 0;
    width: 100%;
    height: 39px;
    background: var(--footer-black);
  }
  .brand {
    position: absolute;
    left: 56px;
    top: 76px;
    line-height: 1.1;
  }
  .brand-name {
    display: block;
    font-size: 36px;
    font-weight: 700;
    color: var(--brand-blue);
    letter-spacing: 0.3px;
  }
  .brand-sub {
    display: block;
    font-size: 35px;
    font-weight: 700;
    color: var(--ink);
    letter-spacing: -0.3px;
  }
  .feature {
    position: absolute;
    left: 58px;
    width: 760px;
    height: 172px;
  }
  .feature-photo {
    position: absolute;
    left: 0; top: 0;
    width: 249px;
    height: 172px;
  }
  .photo-handshake { background: linear-gradient(135deg, #5f7385 0%, #c9a58c 45%, #2b3038 100%); }
  .photo-idea      { background: linear-gradient(120deg, #1d8cb8 0%, #3fb0d6 40%, #1c2430 100%); }
  .photo-meeting   { background: linear-gradient(120deg, #a9c3d2 0%, #dfe8ee 50%, #2f4058 100%); }
  .photo-approval  { background: linear-gradient(160deg, #bfe6f4 0%, #62bce0 55%, #c08b6d 100%); }
  .feature-title {
    position: absolute;
    left: 285px;
    top: 20px;
    font-size: 35px;
    font-weight: 700;
    color: var(--brand-blue);
    letter-spacing: 1.4px;
    line-height: 1;
  }
  .feature-text {
    position: absolute;
    left: 285px;
    top: 66px;
    width: 462px;
    font-size: 17px;
    font-weight: 300;
    line-height: 27px;
    color: var(--body-grey);
  }
</style>
</head>
<body>
<main class="sheet">
  <div class="top-band"></div>

  <header class="brand">
    <span class="brand-name">VOLQ</span>
    <span class="brand-sub">Marketing</span>
  </header>

  <section class="feature" style="top:250px">
    <div class="feature-photo photo-handshake" role="img" aria-label="Photo of two businessmen shaking hands"></div>
    <h2 class="feature-title">PROFESSIONAL</h2>
    <p class="feature-text">Whether it’s automobile, home, life or health coverage, our licensed agents guide you through every option and explain each detail clearly, so you can choose the plan that truly fits your needs.</p>
  </section>

  <section class="feature" style="top:458px">
    <div class="feature-photo photo-idea" role="img" aria-label="Photo of a businessman holding a glowing light bulb in his open hand"></div>
    <h2 class="feature-title">RELIABLE</h2>
    <p class="feature-text">When the unexpected happens, you can rest easy knowing that trusted help is only a phone call away. We answer quickly, follow through on every claim and stay with you until it is settled.</p>
  </section>

  <section class="feature" style="top:667px">
    <div class="feature-photo photo-meeting" role="img" aria-label="Photo of smiling business people meeting at a table"></div>
    <h2 class="feature-title">TRUST</h2>
    <p class="feature-text">Families and businesses across our community have relied on us for years. We build lasting relationships through honest advice, fair pricing and coverage that protects what matters most to you.</p>
  </section>

  <section class="feature" style="top:875px">
    <div class="feature-photo photo-approval" role="img" aria-label="Photo of many hands giving thumbs up against a blue sky"></div>
    <h2 class="feature-title">QUALITY</h2>
    <p class="feature-text">We partner with top-rated carriers to bring you dependable policies at competitive rates. Every plan is reviewed with care, so you receive strong protection and real value year after year.</p>
  </section>

  <div class="bottom-band"></div>
</main>
</body>
</html>
```